I need 2 flyers designed for my business

Both can be similar in design and will have different purposes. I need an education based flyer and I need a government based flyer. The focus of the flyer will be software on the front and services on the back.
These all need to be 8.5x 11 in dimension (they can be full bleed). I would like to be able to print these out if needed. The design needs to look good with our website > www.brelmark.com

The software details are on the website.

```html
<!DOCTYPE html>
<html lang="en">
<head>
<meta charset="utf-8">
<title>Northvale Records – BrelView Flyers</title>
<link rel="stylesheet" href="https://fonts.googleapis.com/css2?family=Poppins:ital,wght@0,400;0,500;0,600;0,700;1,400;1,600;1,800&display=swap">
<style>
  :root {
    --maroon: #8a1c24;
    --maroon-dark: #6e141b;
    --blue: #1aa0e2;
    --blue-light: #5cc2f0;
    --blue-pale: #e6f3fb;
    --navy: #1c3353;
    --steel: #6b8fc9;
    --blush: #e3c7c3;
    --olive: #9a8a3a;
    --text: #333a40;
    --rule: #c9ced3;
    --paper: #ffffff;
    --stage: #eeeff1;
  }
  * { box-sizing: border-box; margin: 0; padding: 0; }
  html, body { width: 867px; height: 1200px; overflow: hidden; background: var(--stage); }
  body { position: relative; font-family: "Poppins", sans-serif; color: var(--text); }

  /* each flyer is built at 867×1200 and set down at 48% */
  .frame { position: absolute; top: 312px; width: 416px; height: 576px; overflow: hidden; box-shadow: 0 4px 14px rgba(0,0,0,0.18); }
  .frame--front { left: 12px; }
  .frame--back { left: 439px; }
  .sheet { position: absolute; left: 0; top: 0; width: 867px; height: 1200px; background: var(--paper); overflow: hidden; transform: scale(0.48); transform-origin: 0 0; }
  .shapes { position: absolute; inset: 0; }

  .brand {
    position: absolute; left: 30px; top: 30px;
    display: flex; align-items: center; gap: 12px;
    color: var(--maroon); font-weight: 600; font-size: 27px; line-height: 1.05; letter-spacing: 0.5px;
  }
  .brand-dot { width: 58px; height: 58px; border-radius: 50%; background: var(--maroon); flex: none; }
  .brand--center { left: 50%; transform: translateX(-50%); top: 28px; }

  /* front */
  .headline {
    position: absolute; right: 32px; top: 322px; text-align: right;
    color: var(--maroon); font-weight: 800; font-style: italic; font-size: 31px; line-height: 33px;
  }
  .tagline {
    position: absolute; right: 32px; top: 460px; text-align: right;
    font-style: italic; font-size: 18px; line-height: 21px; color: var(--text);
  }
  .software { position: absolute; left: 32px; top: 408px; width: 230px; }
  .software h2 { color: var(--blue); font-size: 27px; font-weight: 700; line-height: 32px; }
  .software p { font-size: 15.5px; line-height: 21px; margin-top: 2px; }

  .product-badge {
    position: absolute; left: 322px; top: 671px; width: 208px; height: 64px;
    border: 4px solid var(--maroon); border-radius: 32px; background: var(--paper);
    display: flex; align-items: center; justify-content: center;
    color: var(--maroon); font-weight: 700; font-size: 33px;
    box-shadow: 0 3px 6px rgba(0,0,0,0.25);
  }
  .module { position: absolute; top: 796px; width: 104px; height: 104px; margin-left: -52px; }
  .module-ring {
    position: absolute; inset: 0; border-radius: 50%;
    border: 6px solid var(--blue); background: var(--paper);
    box-shadow: 0 3px 6px rgba(0,0,0,0.2);
    display: flex; align-items: center; justify-content: center; text-align: center;
    color: var(--maroon); font-weight: 600; font-size: 12.5px; line-height: 13px; padding: 0 8px;
  }
  .module-icon {
    position: absolute; left: 50%; top: -10px; width: 30px; height: 30px; margin-left: -15px;
    border-radius: 50%; background: var(--maroon); border: 2px solid var(--paper);
    display: flex; align-items: center; justify-content: center;
  }
  .module-icon span { width: 12px; height: 10px; border: 2px solid var(--paper); border-radius: 2px; }

  .list-block { position: absolute; top: 962px; }
  .list-block h3 { color: var(--blue); font-size: 27px; font-weight: 700; line-height: 32px; }
  .list-block ul { list-style: none; margin-top: 4px; }
  .list-block li {
    position: relative; padding-left: 19px; font-size: 16px; line-height: 20px;
    border-bottom: 1px solid var(--rule); padding-bottom: 3px; margin-bottom: 4px;
  }
  .list-block li:last-child { border-bottom: none; }
  .list-block li::before {
    content: ""; position: absolute; left: 3px; top: 8px; width: 6px; height: 6px;
    border-radius: 50%; background: var(--maroon);
  }
  .benefits { left: 33px; width: 370px; }
  .provides { left: 470px; width: 365px; }
  .provides li { padding-bottom: 2px; margin-bottom: 3px; font-size: 15.5px; line-height: 20px; }
  .divider { position: absolute; left: 435px; top: 966px; width: 2px; height: 182px; background: var(--maroon); }

  .site { position: absolute; left: 33px; top: 1150px; color: var(--maroon); font-weight: 600; font-size: 17px; }
  .site-rule { position: absolute; left: 218px; right: 32px; top: 1163px; height: 2px; background: var(--blue); }

  /* back */
  .sheet--back { background: linear-gradient(100deg, #ffffff 0%, #f4f5f7 45%, #dfe2e6 100%); }
  .service { position: absolute; left: 0; width: 867px; height: 295px; }
  .service-photo {
    position: absolute; left: 0; top: 0; width: 375px; height: 223px;
    border-radius: 0 112px 112px 0;
    background: linear-gradient(120deg, #1aa0e2 0%, #3db1ea 45%, #8fc6e4 75%, #c9d8e4 100%);
  }
  .service-title {
    position: absolute; left: 32px; top: 84px; width: 320px;
    color: #fff; font-weight: 800; font-style: italic; font-size: 25px; line-height: 28px;
    text-shadow: 0 2px 3px rgba(0,0,0,0.3);
  }
  .service-rule { position: absolute; left: 367px; top: 42px; width: 500px; height: 6px; background: var(--maroon); }
  .service-desc {
    position: absolute; left: 392px; top: 80px; width: 185px;
    color: var(--maroon); font-weight: 600; font-style: italic; font-size: 12.5px; line-height: 20px;
  }
  .service-points { position: absolute; left: 596px; top: 78px; width: 255px; }
  .service-points h4 { color: var(--maroon); font-size: 16.5px; font-weight: 600; line-height: 18px; }
  .service-points ul { list-style: none; margin-top: 4px; }
  .service-points li { position: relative; padding-left: 14px; font-size: 12.5px; line-height: 16px; margin-bottom: 4px; }
  .service-points li::before {
    content: ""; position: absolute; left: 2px; top: 6px; width: 5px; height: 5px;
    border-radius: 50%; background: var(--olive);
  }
  .service-band {
    position: absolute; left: 86px; top: 223px; width: 781px; height: 40px;
    border-radius: 20px 0 0 20px;
    background: linear-gradient(90deg, var(--maroon) 0%, var(--maroon) 55%, #c79a98 100%);
  }
  .service-line { position: absolute; left: 100px; top: 266px; width: 700px; height: 3px; background: var(--blue); }
  .service-dashes {
    position: absolute; left: 808px; top: 266px; width: 59px; height: 3px;
    background: repeating-linear-gradient(90deg, var(--blue) 0 6px, transparent 6px 10px);
  }
  .sales {
    position: absolute; left: 0; right: 0; top: 1026px; text-align: center;
    color: var(--maroon); font-weight: 800; font-style: italic; font-size: 19px;
  }
</style>
</head>
<body>

<div class="frame frame--front">
<main class="sheet sheet--front">
  <svg class="shapes" width="867" height="1200" viewBox="0 0 867 1200">
    <defs>
      <linearGradient id="photoSoft" x1="0" y1="0" x2="1" y2="0">
        <stop offset="0" stop-color="#ffffff"/>
        <stop offset="0.45" stop-color="#c9d3de"/>
        <stop offset="1" stop-color="#7f93ab"/>
      </linearGradient>
      <linearGradient id="photoDark" x1="0" y1="0" x2="1" y2="1">
        <stop offset="0" stop-color="#4d6786"/>
        <stop offset="0.5" stop-color="#213a5c"/>
        <stop offset="1" stop-color="#15294a"/>
      </linearGradient>
      <linearGradient id="bandBlue" x1="0" y1="0" x2="1" y2="0">
        <stop offset="0" stop-color="#1aa0e2"/>
        <stop offset="0.7" stop-color="#2aa8e6"/>
        <stop offset="1" stop-color="#8fd3f5"/>
      </linearGradient>
      <linearGradient id="pillFill" x1="0" y1="0" x2="1" y2="0">
        <stop offset="0" stop-color="#ffffff" stop-opacity="0.55"/>
        <stop offset="0.3" stop-color="#ffffff" stop-opacity="0.92"/>
        <stop offset="1" stop-color="#e6f3fb"/>
      </linearGradient>
      <linearGradient id="innerDisc" x1="0" y1="0" x2="1" y2="0">
        <stop offset="0" stop-color="#e3c7c3"/>
        <stop offset="1" stop-color="#e6f3fb"/>
      </linearGradient>
    </defs>

    <rect x="0" y="0" width="867" height="330" fill="url(#photoSoft)" role="img" aria-label="Soft-focus office background behind the business photo"/>
    <circle cx="444" cy="397" r="192" fill="var(--blue)"/>
    <rect x="444" y="519" width="423" height="69" fill="url(#bandBlue)"/>
    <rect x="544" y="0" width="323" height="312" fill="url(#photoDark)" role="img" aria-label="Businessman in a suit pointing at a floating yellow folder among connected document icons"/>
    <path d="M0 0 H309 V94 A48 48 0 0 1 261 142 H0 Z" fill="#ffffff"/>
    <rect x="0" y="306" width="470" height="69" fill="var(--maroon)"/>
    <path d="M0 375 H320 V588 H0 Z" fill="#ffffff"/>
    <path d="M252 375 H320 V588 H280 A192 192 0 0 1 252 470 Z" fill="var(--blue)"/>
    <path d="M0 375 H262 A192 192 0 0 0 262 588 H0 Z" fill="#ffffff"/>
    <circle cx="416" cy="420" r="88" fill="url(#innerDisc)"/>
    <path d="M471 312 H867 V519 H471 A103.5 103.5 0 0 1 471 312 Z" fill="url(#pillFill)"/>
    <path d="M0 588 H369 A34.5 34.5 0 0 1 369 657 H0 Z" fill="var(--maroon)"/>
    <path d="M330 588 H430 L418 612 H330 Z" fill="var(--steel)" opacity="0.85"/>

    <g fill="none" stroke="var(--blue)" stroke-width="1.6">
      <path d="M392 752 V768 H120 V792"/>
      <path d="M408 752 V772 H245 V792"/>
      <path d="M425 752 V776 H371 V792"/>
      <path d="M441 752 V776 H497 V792"/>
      <path d="M458 752 V772 H623 V792"/>
      <path d="M474 752 V768 H749 V792"/>
    </g>
    <g fill="#ffffff" stroke="var(--navy)" stroke-width="1.6">
      <circle cx="392" cy="750" r="3.5"/>
      <circle cx="408" cy="750" r="3.5"/>
      <circle cx="425" cy="750" r="3.5"/>
      <circle cx="441" cy="750" r="3.5"/>
      <circle cx="458" cy="750" r="3.5"/>
      <circle cx="474" cy="750" r="3.5"/>
    </g>
  </svg>

  <div class="brand"><span class="brand-dot"></span><span>NORTHVALE<br>RECORDS</span></div>

  <h1 class="headline">Transform Your<br>Document Management<br>with Our Cutting<br>-Edge Software</h1>
  <p class="tagline">Streamline Your Workflow, Boost Efficiency,<br>and Save Space</p>

  <section class="software">
    <h2>Software</h2>
    <p>Access all of your records – whether active or inactive – through BrelView, our comprehensive records management software.</p>
  </section>

  <div class="product-badge">BrelView</div>

  <div class="module" style="left:120px"><div class="module-ring">Document Archive</div><div class="module-icon"><span></span></div></div>
  <div class="module" style="left:245px"><div class="module-ring">HR Onboarding</div><div class="module-icon"><span></span></div></div>
  <div class="module" style="left:371px"><div class="module-ring">Electronic Forms &amp; Workflows</div><div class="module-icon"><span></span></div></div>
  <div class="module" style="left:497px"><div class="module-ring">eSigning</div><div class="module-icon"><span></span></div></div>
  <div class="module" style="left:623px"><div class="module-ring">Mileage &amp; Expense Tracking</div><div class="module-icon"><span></span></div></div>
  <div class="module" style="left:749px"><div class="module-ring">Scanning &amp; Database Conversion</div><div class="module-icon"><span></span></div></div>

  <section class="list-block benefits">
    <h3>Benefits</h3>
    <ul>
      <li>Enjoy both web-based access to your records or access them on the go using our mobile app.</li>
      <li>Includes 3rd party integration tools.</li>
      <li>Protects records with disaster recovery and redundancy features.</li>
    </ul>
  </section>

  <div class="divider"></div>

  <section class="list-block provides">
    <h3>BrelView Provides:</h3>
    <ul>
      <li>Electronic forms</li>
      <li>Workflow automation</li>
      <li>Automated system/email notifications</li>
      <li>Full text search capabilities</li>
      <li>Audit tracking (including HIPAA)</li>
      <li>Redaction &amp; annotation capabilities</li>
    </ul>
  </section>

  <p class="site">www.brelmark.com</p>
  <div class="site-rule"></div>
</main>
</div>

<div class="frame frame--back">
<main class="sheet sheet--back">
  <div class="brand brand--center"><span class="brand-dot"></span><span>NORTHVALE<br>RECORDS</span></div>

  <section class="service" style="top:127px">
    <div class="service-rule"></div>
    <div class="service-photo" role="img" aria-label="Hands feeding paper records into a document scanner, tinted blue"></div>
    <h2 class="service-title">Document Scanning Services</h2>
    <p class="service-desc">Fast, efficient process for the conversion of existing paper records to digital archives, increasing access and reducing onsite storage and costs.</p>
    <div class="service-points">
      <h4>Scanning services for any format:</h4>
      <ul>
        <li>Standard Office Documents</li>
        <li>16mm, 35mm Roll Microfilm</li>
        <li>Microfiche (Jackets or COM)</li>
        <li>Large Format Documents/Drawings</li>
      </ul>
    </div>
    <div class="service-band"></div>
    <div class="service-line"></div>
    <div class="service-dashes"></div>
  </section>

  <section class="service" style="top:422px">
    <div class="service-rule"></div>
    <div class="service-photo" role="img" aria-label="Open filing cabinet drawers full of folders, tinted blue"></div>
    <h2 class="service-title">Document Storage Services</h2>
    <p class="service-desc">Solution for offsite document storage and retrieval to effectively store, manage, and safeguard your vital business records and documents.</p>
    <div class="service-points">
      <h4>A local, convenient solution:</h4>
      <ul>
        <li>Free Up Office Space</li>
        <li>Reduce Costs</li>
        <li>Keep Records in a Fireproof, Waterproof &amp; Wind-Safe Facility</li>
      </ul>
    </div>
    <div class="service-band"></div>
    <div class="service-line"></div>
    <div class="service-dashes"></div>
  </section>

  <section class="service" style="top:717px">
    <div class="service-rule"></div>
    <div class="service-photo" role="img" aria-label="Stack of paper files secured with a chain, tinted blue"></div>
    <h2 class="service-title">Secure Document Shredding</h2>
    <p class="service-desc">Safely and cost-effectively destroy unnecessary paperbased documents. One-time or recurring, our solutions are tailored to you.</p>
    <div class="service-points">
      <h4>Destroy Unnecessary Documents:</h4>
      <ul>
        <li>Protect confidential information</li>
        <li>Reduce the cost of managing information that is no longer useful</li>
        <li>Ensure compliance with regulations for information destruction</li>
      </ul>
    </div>
    <div class="service-band"></div>
    <div class="service-line"></div>
    <div class="service-dashes"></div>
  </section>

  <p class="sales">Sales inquiries to (555) 014-2290 or help@northvale.org</p>

  <p class="site">www.brelmark.com</p>
  <div class="site-rule"></div>
</main>
</div>

</body>
</html>
```